Form By Tammi - Health and Wellness Business Card and Logo

I need a business card design with a logo for my business you can check out at www.formbytammi.com. I want something more original, simplistic, and memorable than the basic logo I have on my site currently. I am a health and wellness coach and I offer mindset coaching and nutrition plans. I like the colour teal and dark grey/black for my theme colours. I emphasize growth, longterm change, and the whole package of "healthy mind, healthy body, healthy life". I had played around the idea of intertwining 3 T's or incorporating growth (leaves etc.) into my design. I want my expertise and experience to show through. In one glance I want people to understand with confidence I can help them accomplish anything they set their minds to. I look forward to seeing what everyone comes up with!

Industry/Entity Type

Health And Wellness

Contact Information for Business Card

Form By Tammi
Tammi Orlund
BSc, Health & Wellness Coach
"Manifest your best"
www.formbytammi.com
formbytammi@quillmail.com
613-472-0916
[Instagram logo] @tammiorlund

Colors
33b8a4
ffffff
333333
000000

Requirements
Must have
• A memorable and unique logo for my business!
Nice to have
• Could have the phrase "Are you unhappy with your body and state of health?" or "It takes the right skills to develop habits in order to create long term change. I can help you get there."

```html
<!DOCTYPE html>
<html lang="en">
<head>
<meta charset="utf-8">
<title>Form By Tammi – Business Card</title>
<link rel="stylesheet" href="https://fonts.googleapis.com/css2?family=Open+Sans:wght@300;400;700&display=swap">
<style>
  :root {
    --teal: #26b9a4;
    --white: #ffffff;
    --ink: #5b5b5b;
    --ink-soft: #8a8a8a;
    --mist: #e7e8e9;
    --stage: #2f2f2f;
  }
  * { margin: 0; padding: 0; box-sizing: border-box; }
  html, body {
    width: 1200px; height: 894px; overflow: hidden;
    background: var(--stage);
    font-family: "Open Sans", Arial, sans-serif;
  }
  .canvas { position: relative; width: 1200px; height: 894px; }
  .card {
    position: absolute; width: 600px; height: 343px;
    box-shadow: 0 10px 30px rgba(0,0,0,.45);
  }
  .card--front { left: 140px; top: 110px; background: var(--teal); }
  .card--back  { left: 470px; top: 420px; background: var(--white); }

  .brand { display: flex; align-items: center; gap: 12px; font-weight: 300; white-space: nowrap; }
  .brand__dot { border-radius: 50%; flex: none; }

  .card--front .brand {
    position: absolute; left: 0; right: 0; top: 50%; transform: translateY(-50%);
    justify-content: center; color: var(--white); font-size: 40px;
  }
  .card--front .brand__dot { width: 30px; height: 30px; background: var(--white); }

  .card--back .brand {
    position: absolute; left: 36px; top: 42px; color: var(--ink); font-size: 29px;
  }
  .card--back .brand__dot { width: 26px; height: 26px; background: var(--teal); }

  .backdrop-disc {
    position: absolute; left: 90px; top: 128px;
    width: 180px; height: 180px; border-radius: 50%; background: var(--mist);
  }

  .contact { position: absolute; right: 34px; top: 34px; text-align: right; }
  .contact__name {
    color: var(--teal); font-weight: 700; font-size: 21px; letter-spacing: .5px;
    text-transform: uppercase; line-height: 1.1;
  }
  .contact__role { color: var(--ink-soft); font-size: 11.5px; margin-top: 2px; }
  .contact__list { list-style: none; margin-top: 20px; }
  .contact__item {
    display: flex; justify-content: flex-end; align-items: center; gap: 12px;
    color: var(--ink); font-size: 19px; line-height: 1.35;
  }
  .contact__icon { width: 18px; height: 18px; flex: none; }
  .contact__icon path, .contact__icon circle { fill: none; stroke: var(--teal); stroke-width: 2; }
  .contact__icon .solid { fill: var(--teal); stroke: none; }
</style>
</head>
<body>
<main class="canvas">
  <section class="card card--front" aria-label="Card front">
    <div class="brand"><span class="brand__dot"></span><span>Form By Tammi</span></div>
  </section>

  <section class="card card--back" aria-label="Card back">
    <div class="brand"><span class="brand__dot"></span><span>Form By Tammi</span></div>
    <div class="backdrop-disc" aria-hidden="true"></div>

    <div class="contact">
      <p class="contact__name">Tammi Orlund</p>
      <p class="contact__role">BSc, Health &amp; Wellness Coach</p>
      <ul class="contact__list">
        <li class="contact__item"><span>613-472-0916</span>
          <svg class="contact__icon" viewBox="0 0 24 24" aria-hidden="true"><path class="solid" d="M6.6 2.5l3 3.2-1.8 2.6c1.3 2.9 3.5 5.1 6.4 6.6l2.6-1.8 3.2 3-1.6 3.4C10.6 19.2 4.6 13.2 3.2 4.1z"/></svg></li>
        <li class="contact__item"><span>www.formbytammi.com</span>
          <svg class="contact__icon" viewBox="0 0 24 24" aria-hidden="true"><circle cx="12" cy="12" r="9"/><path d="M3 12h18M12 3c-4 4.5-4 13.5 0 18M12 3c4 4.5 4 13.5 0 18"/></svg></li>
        <li class="contact__item"><span>formbytammi@quillmail.com</span>
          <svg class="contact__icon" viewBox="0 0 24 24" aria-hidden="true"><path class="solid" d="M2 5h20v14H2z"/><path d="M2.5 5.5l9.5 8 9.5-8" style="stroke:#fff"/></svg></li>
      </ul>
    </div>
  </section>
</main>
</body>
</html>
```